Email Signature Design

Please design an email signature, the below is an example of our current design;
___

CORMACK ESTATE HOLDINGS PTY LTD
BARNABY CORMACK
Licensed Strata and Community Manager

164 Tallowood Street,
ULTIMO NSW 2007

P: 02.9376.5820 F: 9463.7208
Website: www.cormackestates.com.au

This e-mail message and accompanying data may contain information that is confidential and private. If you are not the intended recipient, the use, dissemination, distribution or copying of this message or data is prohibited.

If you have received this e-mail in error please notify us immediately and delete all material pertaining to this e-mail. strata@cormackestates.com.au

___

We would like to incorporate our logo and company colours, you can view the colours and feel of image at www.cormackestates.com.au

Industry/Entity Type

It Company

Requirements
Must have
• use of logo and company colours (image)

```html
<!DOCTYPE html>
<html lang="en">
<head>
<meta charset="utf-8">
<title>Cormack Estate Holdings – Email Signature</title>
<link href="https://fonts.googleapis.com/css2?family=Arimo:wght@400;700&display=swap" rel="stylesheet">
<style>
  :root {
    --backdrop: #bdbcbd;
    --band: #656364;
    --paper: #fbfbf8;
    --paper-lower: #f1f1ee;
    --olive: #6c7830;
    --charcoal: #5e5c5d;
    --text: #3f3f3f;
    --beige: #e0cf98;
  }
  * { box-sizing: border-box; margin: 0; padding: 0; }
  html, body {
    width: 1200px; height: 900px; overflow: hidden;
    background: var(--backdrop);
    font-family: "Arimo", Arial, sans-serif;
  }
  .signature {
    position: absolute; left: 109px; top: 157px;
    width: 982px; height: 584px;
    background: var(--paper);
    box-shadow: 6px 8px 10px rgba(0,0,0,0.25);
    overflow: hidden;
  }
  .band { position: absolute; left: 0; width: 100%; background: var(--band); }
  .band--top { top: 0; height: 22px; }
  .band--bottom { bottom: 0; height: 19px; }
  .lower-panel {
    position: absolute; left: 0; top: 334px; width: 100%; height: 231px;
    background: var(--paper-lower);
  }
  .divider {
    position: absolute; left: 60px; top: 331px; width: 873px; height: 3px;
    background: var(--olive);
  }
  .brand {
    position: absolute; left: 76px; top: 105px;
  }
  .brand__mark {
    width: 118px; height: 118px; background: var(--olive);
  }
  .brand__name {
    margin-top: 32px;
    font-size: 25px; font-weight: 700; color: var(--olive);
    letter-spacing: 0.2px; white-space: nowrap;
  }
  .contact {
    position: absolute; left: 546px; top: 70px;
    color: var(--charcoal); font-size: 17px; line-height: 27px;
    white-space: nowrap;
  }
  .contact__company { font-weight: 700; font-size: 16.5px; letter-spacing: 0.4px; }
  .contact__name { font-weight: 700; font-size: 19px; color: var(--olive); letter-spacing: 0.3px; }
  .contact__gap { height: 24px; }
  .contact__web { font-weight: 700; color: var(--olive); }
  .disclaimer {
    position: absolute; left: 82px; top: 363px; width: 860px;
    font-size: 18.5px; line-height: 30px; color: var(--text);
  }
  .disclaimer p { white-space: nowrap; }
  .disclaimer p + p { margin-top: 28px; }
  .disclaimer__email { font-weight: 700; color: var(--olive); }
  .corner-mark {
    position: absolute; left: 855px; top: 465px;
    width: 78px; height: 78px; background: var(--olive); opacity: 0.25;
  }
</style>
</head>
<body>
  <div class="signature">
    <div class="band band--top"></div>
    <div class="lower-panel"></div>
    <div class="divider"></div>

    <div class="brand">
      <div class="brand__mark"></div>
      <div class="brand__name">CORMACK ESTATE HOLDINGS</div>
    </div>

    <div class="contact">
      <div class="contact__company">CORMACK ESTATE HOLDINGS PTY LTD</div>
      <div class="contact__name">BARNABY CORMACK</div>
      <div>Licensed Strata and Community Manager</div>
      <div class="contact__gap"></div>
      <div>164 Tallowood Street,</div>
      <div>ULTIMO NSW 2007</div>
      <div class="contact__gap"></div>
      <div>P: 02.9376.5820 F: 9463.7208</div>
      <div class="contact__web">Website: www.cormackestates.com.au</div>
    </div>

    <div class="disclaimer">
      <p>This email message and accompanying data may contain information that is<br>
      confidential and private. If you are not the intended recipinet, the use, dissemination,<br>
      distribution or copying of this message or data is probited.</p>
      <p>If you have received this e-mail in error please notify us immediately and delete all<br>
      material pertaining to this email: <span class="disclaimer__email">strata@cormackestates.com.au</span></p>
    </div>

    <div class="corner-mark"></div>
    <div class="band band--bottom"></div>
  </div>
</body>
</html>
```